Lawn Maintenance Company needs attractive add for local newspaper

My company Fennick Yard Service offers many lawn and yard services but I want this add to focus on one specific service we offer.
- Lawn Fertilizer and Weed Control -

This will be an add for our local newspaper, likely a 1/4 page

Some more information about this service.
Our customers generally call us when their lawn is over run with weeds or is performing poorly. Most of the time we set them up with a program and we return to their property every 4 - 5 weeks for another application. 95% of our customers return the following year for the same program. If the customer wishes we will also do a one time application

email: fennickyardservice@example.net
phone: call or text 555-418-7390

Target Market(s)

- Local small towns, populations less than 20,000
- Residential and Commercial customers with lawns
- People who are using the competitors service and aren't happy with it

Industry/Entity Type

Lawn Care

Requirements
Must have
• Must include our logo, email address and phone number
• - Logo
• - Email address and phone number (call or text)
• - Must focus on the service we want to sell (fertilizer and weed control)
Nice to have
• Some phrases or words that should be included, does not need to be word for word as long as the point is made
• - We service both Residential & Commercial properties
• - We offer professional service that can dramatically improve your lawn whether you are looking for a single application or a season long fertilizer/weed control program
• - Our lawn techs are licensed and certified applicators
Should not have
• I do not want any stock pictures of people, houses or equipment.

```html
<!DOCTYPE html>
<html lang="en">
<head>
<meta charset="utf-8">
<title>Fennick Yard Service – Lawn Fertilizer and Weed Control</title>
<link rel="stylesheet" href="https://fonts.googleapis.com/css2?family=Arimo:wght@400;700&display=swap">
<style>
  :root {
    --paper: #ffffff;
    --ink: #111111;
    --coral: #c8635a;
    --slate-green: #4a6b5d;
    --grass: #63b346;
    --edge: #9a9a9a;
  }
  * { margin: 0; padding: 0; box-sizing: border-box; }
  html, body {
    width: 1200px; height: 800px; overflow: hidden;
    background: var(--paper);
  }
  .ad {
    position: relative; width: 1200px; height: 800px;
    background: var(--paper);
    border: 1px solid var(--edge);
    font-family: "Arimo", Arial, sans-serif;
    color: var(--ink);
  }
  .brand {
    position: absolute; left: 50px; top: 40px; width: 646px; height: 400px;
    display: flex; flex-direction: column; justify-content: center; align-items: center;
    color: var(--grass); font-weight: 700; text-align: center; line-height: 1;
  }
  .brand-name { font-size: 108px; letter-spacing: 2px; }
  .brand-sub { font-size: 54px; letter-spacing: 4px; margin-top: 14px; }
  .email {
    position: absolute; left: 61px; top: 482px;
    font-size: 33px; color: var(--coral); white-space: nowrap;
  }
  .service-card {
    position: absolute; left: 738px; top: 40px; width: 422px; height: 485px;
    border: 3px solid var(--slate-green); border-radius: 20px;
    text-align: center; padding: 0 14px;
  }
  .service-title {
    color: var(--coral); font-weight: 400; font-size: 38px; line-height: 41px;
    margin-top: 16px;
  }
  .service-point {
    font-size: 29px; line-height: 31px; padding: 8px 0 10px;
  }
  .service-point + .service-point { border-top: 2px solid var(--slate-green); }
  .service-point:first-of-type { padding-top: 10px; }
  .call-band {
    position: absolute; left: 40px; top: 537px; width: 1120px; height: 221px;
    background: var(--grass); text-align: center; font-weight: 700;
  }
  .call-label { font-size: 66px; line-height: 1; margin-top: 10px; }
  .call-number { font-size: 172px; line-height: 1; letter-spacing: -3px; margin-top: 2px; }
</style>
</head>
<body>
<main class="ad">
  <div class="brand">
    <span class="brand-name">FENNICK</span>
    <span class="brand-sub">YARD SERVICE</span>
  </div>

  <p class="email">Email: fennickyardservice@example.net</p>

  <section class="service-card">
    <h1 class="service-title">Lawn Fertilizer<br>and Weed Control</h1>
    <p class="service-point">We service both<br>Residential &amp; Commercial<br>properties</p>
    <p class="service-point">We offer single<br>applications or season<br>long fertilizer/weed<br>control programs</p>
    <p class="service-point">All of our technicians<br>are certified by<br>Prairie Environment Board</p>
  </section>

  <section class="call-band">
    <p class="call-label">Call or Text:</p>
    <p class="call-number">555-418-7390</p>
  </section>
</main>
</body>
</html>
```